Updated Business Card for Optometry Practice

We're a growing optometry practice that is moving to a beautiful new office and we want to update our business card. We just updated our logo so the new card should reflect the new logo. Our practice continually invests in state of the art instruments to help us provide eye care that is thorough, comfortable, efficient and educational.

I've attached our current card and logo. You can reference this for the information I would like on the card. The tag line on the back is "We're changing the way you see."

Upon completion of this project we will need (amongst other formats) Photoshop files of the card so I can change employee names to print cards for each employee.

```html
<!DOCTYPE html>
<html lang="en">
<head>
<meta charset="UTF-8">
<title>Brightwater Family Eyecare – Business Card</title>
<link rel="stylesheet" href="https://fonts.googleapis.com/css2?family=Montserrat:wght@400;500;700;800&display=swap">
<style>
  :root {
    --navy: #15284b;
    --gold: #d6b132;
    --white: #ffffff;
    --ink: #1b1b1b;
    --mist: #e2e2e4;
    --stage: #3a3a3a;
  }
  * { box-sizing: border-box; margin: 0; padding: 0; }
  html, body {
    width: 1200px; height: 689px; overflow: hidden;
    background: var(--stage);
    font-family: "Montserrat", Arial, sans-serif;
  }
  .canvas {
    position: relative; width: 1200px; height: 689px;
    display: flex; align-items: center; justify-content: center; gap: 40px;
  }
  .card {
    position: relative; width: 540px; height: 309px; overflow: hidden;
  }
  .card--front { background: var(--navy); display: flex; align-items: center; justify-content: center; }
  .card--back { background: var(--white); }

  .brand { display: flex; align-items: center; gap: 12px; font-weight: 700; }
  .brand__dot { border-radius: 50%; flex: none; }
  .card--front .brand { color: var(--white); font-size: 34px; letter-spacing: 0.5px; }
  .card--front .brand__dot { width: 26px; height: 26px; background: var(--gold); }
  .front__deco {
    position: absolute; width: 230px; height: 230px; border-radius: 50%;
    border: 26px solid rgba(255,255,255,0.05); left: 155px; top: 40px;
  }

  .back__deco {
    position: absolute; width: 170px; height: 170px; border-radius: 50%;
    border: 22px solid var(--mist); right: 36px; top: -20px;
  }
  .card--back .brand {
    position: absolute; left: 34px; top: 40px; color: var(--navy); font-size: 21px;
  }
  .card--back .brand__dot { width: 16px; height: 16px; background: var(--navy); }

  .person { position: absolute; left: 34px; top: 120px; }
  .person__name { font-weight: 800; font-size: 22px; letter-spacing: 0.3px; color: var(--navy); }
  .person__name .surname { color: var(--gold); }
  .person__role { font-weight: 500; font-size: 14px; color: var(--gold); margin-top: 2px; }

  .contact { position: absolute; left: 34px; bottom: 30px; list-style: none; }
  .contact li { display: flex; align-items: center; gap: 9px; font-size: 12.5px; color: var(--ink); line-height: 22px; }
  .contact svg { width: 13px; height: 13px; fill: var(--navy); flex: none; }

  .address { position: absolute; right: 30px; bottom: 34px; text-align: right; font-size: 12.5px; line-height: 19px; color: var(--ink); }
  .address__org { color: var(--gold); font-weight: 700; font-size: 13.5px; }
</style>
</head>
<body>
<main class="canvas">
  <section class="card card--front" aria-label="Card front">
    <div class="front__deco"></div>
    <div class="brand"><span class="brand__dot"></span>Brightwater Family Eyecare</div>
  </section>

  <section class="card card--back" aria-label="Card back">
    <div class="back__deco"></div>
    <div class="brand"><span class="brand__dot"></span>Brightwater Family Eyecare</div>

    <div class="person">
      <p class="person__name">DANIEL <span class="surname">OSTROW, OD</span></p>
      <p class="person__role">Optometrist</p>
    </div>

    <ul class="contact">
      <li><svg viewBox="0 0 24 24"><path d="M6.6 10.8a15.1 15.1 0 0 0 6.6 6.6l2.2-2.2c.3-.3.7-.4 1-.2 1.1.4 2.3.6 3.6.6.6 0 1 .4 1 1V20c0 .6-.4 1-1 1A17 17 0 0 1 3 4c0-.6.4-1 1-1h3.5c.6 0 1 .4 1 1 0 1.3.2 2.5.6 3.6.1.3 0 .7-.2 1z"/></svg>(555) 014-2287</li>
      <li><svg viewBox="0 0 24 24"><path d="M2 5h20v14H2zm2 2v.5l8 5 8-5V7zm0 2.8V17h16V9.8l-8 5z"/></svg>dan@brightwatereyecare.com</li>
      <li><svg viewBox="0 0 24 24"><path d="M12 2a10 10 0 1 0 0 20 10 10 0 0 0 0-20zm6.9 6h-3a15 15 0 0 0-1.3-3.9A8 8 0 0 1 18.9 8zM12 4c.8 1.2 1.5 2.5 1.9 4h-3.8c.4-1.5 1.1-2.8 1.9-4zM4.3 14a8 8 0 0 1 0-4h3.4a16 16 0 0 0 0 4zm.8 2h3a15 15 0 0 0 1.3 3.9A8 8 0 0 1 5.1 16zm3-8h-3a8 8 0 0 1 4.3-3.9C8.8 5.3 8.4 6.6 8.1 8zM12 20c-.8-1.2-1.5-2.5-1.9-4h3.8c-.4 1.5-1.1 2.8-1.9 4zm2.3-6H9.7a14 14 0 0 1 0-4h4.6a14 14 0 0 1 0 4zm.3 5.9c.6-1.2 1-2.5 1.3-3.9h3a8 8 0 0 1-4.3 3.9zm1.7-5.9a16 16 0 0 0 0-4h3.4a8 8 0 0 1 0 4z"/></svg>www.brightwatereyecare.com</li>
    </ul>

    <address class="address" style="font-style:normal">
      <p class="address__org">Brightwater Family Eyecare</p>
      <p>2710 Harlan Ridge Blvd #204</p>
      <p>Brightwater, MO 63000</p>
    </address>
  </section>
</main>
</body>
</html>
```